Business Card for a Wedding Films Business

We require a business card design for our business 'Lewis Marrow Wedding Films'. The logo needs to look classy and high end.

Target Market(s)

Wedding Couples

Contact Information for Business Card

Lewis Marrow Wedding Films
07312 605 227
films@lewismarrowreels.com
www.lewismarrowreels.com

Facebook: @lewismarrowweddingfilms
Instagram: @lewismarrowfilms

Font styles to use
Sans Serif

Requirements
Must have
• Social media icons - Facebook and Instagram

```html
<!DOCTYPE html>
<html lang="en">
<head>
<meta charset="utf-8">
<title>Lewis Marrow Wedding Films – Business Card</title>
<link rel="stylesheet" href="https://fonts.googleapis.com/css2?family=Jost:wght@500&family=Arimo:wght@400&display=swap">
<style>
  :root {
    --backdrop: #b8b8b8;
    --ink: #0a0a0a;
    --card-dark: #111111;
    --paper: #ffffff;
  }
  * { margin: 0; padding: 0; box-sizing: border-box; }
  html, body { width: 1200px; height: 801px; overflow: hidden; }
  body { background: var(--backdrop); position: relative; }

  .card { position: absolute; top: 274px; width: 444px; height: 263px; overflow: hidden; }
  .card--front { left: 153px; background: var(--paper); color: var(--ink); }
  .card--back { left: 625px; background: var(--card-dark); color: var(--paper); }

  .front__band { position: absolute; left: 368px; top: 0; width: 76px; height: 100%; background: var(--ink); }

  .wordmark { position: absolute; text-align: center; font-family: "Jost", sans-serif; font-weight: 500; text-transform: uppercase; }
  .wordmark__name { display: block; white-space: nowrap; }
  .wordmark__tag { display: block; white-space: nowrap; }

  .card--front .wordmark { left: 20px; top: 51px; width: 246px; }
  .card--front .wordmark__name { font-size: 24px; letter-spacing: 0.2em; line-height: 1; }
  .card--front .wordmark__tag { font-size: 11px; letter-spacing: 0.36em; margin-top: 9px; }

  .card--back .wordmark { left: 0; top: 155px; width: 444px; }
  .card--back .wordmark__name { font-size: 29px; letter-spacing: 0.2em; line-height: 1; }
  .card--back .wordmark__tag { font-size: 12.5px; letter-spacing: 0.38em; margin-top: 9px; }

  .brand-mark { position: absolute; font-family: "Jost", sans-serif; font-weight: 500; text-transform: uppercase; text-align: center; line-height: 1.3; }
  .card--front .brand-mark { left: 368px; top: 176px; width: 76px; color: var(--paper); font-size: 11px; letter-spacing: 0.12em; }
  .card--back .brand-mark { left: 0; top: 100px; width: 444px; color: var(--paper); font-size: 13px; letter-spacing: 0.3em; }

  .contact { position: absolute; left: 28px; list-style: none; font-family: "Arimo", sans-serif; font-size: 12.6px; line-height: 16px; }
  .contact--direct { top: 143px; }
  .contact--social { top: 201px; }
  .contact__item { display: flex; align-items: center; gap: 5px; white-space: nowrap; }
  .contact__icon { width: 12px; height: 12px; flex: none; }
  .contact__chip { width: 12px; height: 12px; flex: none; background: var(--ink); }
  .contact__chip--round { border-radius: 50%; }
</style>
</head>
<body>
  <section class="card card--front" aria-label="Business card front">
    <div class="front__band"></div>
    <div class="brand-mark">Lewis<br>Marrow</div>

    <div class="wordmark">
      <span class="wordmark__name">Lewis Marrow</span>
      <span class="wordmark__tag">Wedding Films</span>
    </div>

    <ul class="contact contact--direct">
      <li class="contact__item">
        <svg class="contact__icon" viewBox="0 0 24 24" aria-hidden="true"><path fill="currentColor" d="M6.6 10.8a15.5 15.5 0 0 0 6.6 6.6l2.2-2.2c.3-.3.7-.4 1-.2 1.1.4 2.3.6 3.6.6.6 0 1 .4 1 1V20c0 .6-.4 1-1 1A17 17 0 0 1 3 4c0-.6.4-1 1-1h3.5c.6 0 1 .4 1 1 0 1.3.2 2.5.6 3.6.1.3 0 .7-.2 1z"/></svg>
        07312 605 227
      </li>
      <li class="contact__item">
        <svg class="contact__icon" viewBox="0 0 24 24" aria-hidden="true"><path fill="currentColor" d="M2 5h20v14H2z"/><path fill="none" stroke="#fff" stroke-width="1.8" d="M2.5 5.5 12 13l9.5-7.5"/></svg>
        films@lewismarrowreels.com
      </li>
      <li class="contact__item">
        <svg class="contact__icon" viewBox="0 0 24 24" aria-hidden="true"><g fill="none" stroke="currentColor" stroke-width="1.8"><circle cx="12" cy="12" r="10"/><ellipse cx="12" cy="12" rx="4.5" ry="10"/><path d="M2 12h20M4 7h16M4 17h16"/></g></svg>
        www.lewismarrowreels.com
      </li>
    </ul>

    <ul class="contact contact--social">
      <li class="contact__item"><span class="contact__chip"></span>@lewismarrowweddingfilms</li>
      <li class="contact__item"><span class="contact__chip contact__chip--round"></span>@lewismarrowfilms</li>
    </ul>
  </section>

  <section class="card card--back" aria-label="Business card back">
    <div class="brand-mark">Lewis Marrow</div>
    <div class="wordmark">
      <span class="wordmark__name">Lewis Marrow</span>
      <span class="wordmark__tag">Wedding Films</span>
    </div>
  </section>
</body>
</html>
```